Brook Forge - Crypto Currency Miner Powered by Renewable Energy Website

We Need Web Pages Design for Website for Crypto Currency Miner

Serivices include:
Mining Rig Sales
Housing for Rigs turnkey on renewable energy grid
Cloud Mining term packages
Updates

http://www.vaultrigratings.example (Competitors sites)

Target Market(s)

Investers for Mining Rigs and terms for 1,2 or 3 years of Hash rate

Industry/Entity Type

Mining

Number of Pages Required

5+ page

Font styles to use
Sans Serif

Colors
add136
9bcb3c
606060
474747
ffc214
cadf82
fbee3e
876aae
6b449b

Requirements
Must have
• Pictures of Solar, Wind and power Factor Correction units
Nice to have
• e-commerce platform so contract terms can be purchased through website
Should not have
• Heavy construction equipment

```html
<!DOCTYPE html>
<html lang="en">
<head>
<meta charset="utf-8">
<title>Brook Forge – Crypto Currency Miner</title>
<link href="https://fonts.googleapis.com/css2?family=Lato:wght@400;700;900&display=swap" rel="stylesheet">
<style>
:root{
  --green:#8cc43c;
  --green-dark:#6fa82a;
  --ink:#333333;
  --text:#474747;
  --muted:#606060;
  --dark:#3a3a3a;
  --yellow:#f0b414;
  --ring:#e6b416;
  --red:#d0121b;
  --white:#ffffff;
}
*{margin:0;padding:0;box-sizing:border-box}
html,body{width:1200px;height:2769px;overflow:hidden;background:var(--white)}
body{font-family:'Lato',sans-serif;color:var(--text);position:relative}
.abs{position:absolute}

/* header */
.site-header{left:0;top:0;width:1200px;height:135px;background:var(--white)}
.brand{left:74px;top:42px;display:flex;align-items:center;gap:12px}
.brand-dot{width:50px;height:50px;border-radius:50%;background:var(--green)}
.brand-name{font-weight:900;font-size:30px;color:var(--muted);letter-spacing:-0.5px}
.main-nav{right:74px;top:60px;display:flex;gap:0}
.main-nav a{font-size:13px;font-weight:700;color:var(--ink);text-decoration:none;margin-left:46px;text-transform:uppercase}
.main-nav a.active{color:var(--green)}

/* hero */
.hero{left:0;top:135px;width:1200px;height:530px;
  background:linear-gradient(180deg,#c9a36a 0%,#e2b77a 30%,#a38266 55%,#4c4f5c 75%,#3a3f4e 100%)}
.hero-title{left:74px;top:318px;height:51px;padding:0 16px;background:rgba(40,40,40,.85);
  color:var(--white);font-weight:900;font-size:40px;line-height:51px}
.hero-sub{left:74px;top:375px;width:513px;height:77px;padding:8px 16px;background:rgba(40,40,40,.75);
  color:var(--white);font-size:20px;line-height:30px}
.hero-dots{left:562px;top:618px;display:flex;gap:7px}
.hero-dots span{width:12px;height:12px;border-radius:50%;background:var(--white)}
.hero-dots span.on{background:var(--green)}

/* buttons */
.btn{display:inline-block;background:var(--green);color:var(--white);font-weight:900;font-size:14px;
  text-transform:uppercase;border-radius:22px;text-align:center;text-decoration:none}

/* about */
.about-mark{left:89px;top:757px;width:302px;display:flex;flex-direction:column;align-items:center;gap:18px}
.about-dot{width:118px;height:118px;border-radius:50%;background:var(--green)}
.about-name{font-weight:900;font-size:46px;color:var(--muted);letter-spacing:-1px}
.about-body{left:436px;top:706px;width:686px}
.section-h{font-weight:700;font-size:33px;color:var(--ink)}
.copy{font-size:15.5px;line-height:28.6px;color:var(--text)}
.about-body .copy{margin-top:14px}
.about-btn{left:436px;top:945px;width:151px;height:43px;line-height:43px}

/* crypto band */
.crypto-band{left:0;top:1074px;width:1200px;height:390px;
  clip-path:polygon(0 0,100% 74px,100% 100%,0 100%);
  background:linear-gradient(120deg,#2f3235 0%,#4a4c4e 45%,#3b3d3f 100%)}
.crypto-body{left:109px;top:1162px;width:700px}
.crypto-body .section-h{color:var(--white);font-size:32px}
.crypto-body .copy{color:#e8e8e8;margin-top:14px;font-size:15px}
.crypto-btn{left:109px;top:1360px;width:151px;height:43px;line-height:43px}
.phone{left:877px;top:1076px;width:159px;height:331px}

/* why us */
.why-head{left:0;top:1505px;width:1200px;text-align:center}
.why-lead{left:0;top:1566px;width:1200px;text-align:center;font-size:15.5px;color:var(--ink)}
.feature{top:1616px;width:300px;text-align:center}
.feature-icon{width:110px;height:110px;border-radius:50%;border:3px solid var(--ring);margin:0 auto;
  display:flex;align-items:center;justify-content:center}
.feature-title{margin-top:28px;font-weight:700;font-size:21px;color:var(--green)}
.feature .copy{font-size:14.5px;line-height:24px;margin-top:6px;color:var(--ink)}
.feature-link{display:block;margin-top:8px;font-weight:700;font-size:14.5px;color:var(--red);text-decoration:none}

/* blog band */
.blog-band{left:0;top:1916px;width:1200px;height:390px;background:var(--dark);
  clip-path:polygon(0 69px,100% 0,100% 100%,0 100%)}
.blog-body{left:74px;top:2018px;width:600px}
.blog-body .section-h{color:var(--white);font-size:32px}
.blog-kicker{margin-top:10px;font-weight:900;font-size:15px;color:var(--yellow);text-transform:uppercase}
.blog-body .copy{color:#ececec;font-size:15px;line-height:26px;margin-top:4px}
.blog-btn{left:76px;top:2208px;width:153px;height:42px;line-height:42px}
.blog-photo{left:703px;top:1990px;width:423px;height:273px;
  background:radial-gradient(circle at 50% 55%,#1f8a6a 0%,#0f4a3e 45%,#1d2a26 75%),#1d2a26}

/* subscribe */
.sub-head{left:0;top:2343px;width:1200px;text-align:center}
.sub-lead{left:0;top:2403px;width:1200px;text-align:center;font-size:15.5px;color:var(--ink)}
.sub-form{left:343px;top:2446px;width:512px;height:48px;border:1px solid #d6d6d6;border-radius:24px;
  box-shadow:0 2px 4px rgba(0,0,0,.12);background:var(--white)}
.sub-form .field{position:absolute;left:22px;top:0;line-height:46px;font-size:13px;color:var(--ink)}
.sub-form .btn{position:absolute;right:5px;top:5px;width:89px;height:36px;line-height:36px;font-size:13px}

/* footer */
.site-footer{left:0;top:2581px;width:1200px;height:188px;background:var(--dark)}
.footer-mark{left:560px;top:2543px;width:80px;height:80px;border-radius:50%;background:var(--white);
  border:4px solid var(--green);display:flex;align-items:center;justify-content:center;
  font-weight:900;font-size:11px;color:var(--green)}
.footer-nav{left:0;top:2645px;width:1200px;display:flex;justify-content:center;gap:44px}
.footer-nav a{color:var(--white);font-size:12.5px;font-weight:700;text-decoration:none;text-transform:uppercase}
.copyright{left:0;top:2675px;width:1200px;text-align:center;font-size:12px;color:#9a9a9a}
.social{left:0;top:2709px;width:1200px;display:flex;justify-content:center;gap:18px}
.social span{width:18px;height:18px;border-radius:50%;background:#8a8a8a}
</style>
</head>
<body>

<header class="site-header abs">
  <div class="brand abs"><span class="brand-dot"></span><span class="brand-name">Brook Forge</span></div>
  <nav class="main-nav abs">
    <a class="active" href="#">Home</a><a href="#">About Us</a><a href="#">Services</a><a href="#">Why Us?</a><a href="#">Blog</a><a href="#">Contact Us</a>
  </nav>
</header>

<section class="hero abs" role="img" aria-label="Wind turbines and solar panel arrays in front of a city skyline at sunset"></section>
<h1 class="hero-title abs">THE BROOK FORGE</h1>
<p class="hero-sub abs">Vestibulum ante ipsum primis in faucibus orci luctus et ultrices posuere cubilia..</p>
<div class="hero-dots abs"><span class="on"></span><span></span><span></span><span></span></div>

<div class="about-mark abs"><span class="about-dot"></span><span class="about-name">Brook Forge</span></div>
<div class="about-body abs">
  <h2 class="section-h">About the Brook Forge</h2>
  <p class="copy">Aliquam molestie, mi et imperdiet euismod, dui purus auctor tellus, et interdum lacus lectus et ante. Sed accumsan sollicitudin sapien, sit amet adipiscing turpis gravida ac. In congue, neque ac lobortis volutpat, libero mauris varius mi, vitae suscipit ipsum ligula vitae risus. Duis aliquam nibh a dui iaculis viverra id a velit. Vivamus egestas risus in magna varius commodo.<br>Sed semper viverra egestas.</p>
</div>
<a class="btn about-btn abs" href="#">Read More</a>

<section class="crypto-band abs" role="img" aria-label="Close-up of stacked crypto coins on a dark background"></section>
<div class="crypto-body abs">
  <h2 class="section-h">Crypto Currency Miner</h2>
  <p class="copy">Aliquam molestie, mi et imperdiet euismod, dui purus auctor tellus, et interdum lacus lectus et ante. Sed accumsan sollicitudin sapien, sit amet adipiscing turpis gravida ac. In congue, neque ac lobortis volutpat, libero mauris varius mi, vitae suscipit ipsum ligula vitae risus. Duis aliquam nibh a dui iaculis viverra id a velit.</p>
</div>
<a class="btn crypto-btn abs" href="#">Read More</a>
<div class="phone abs" role="img" aria-label="Smartphone showing the Brook Forge app screen"
  style="border-radius:22px;background:linear-gradient(180deg,#f2f2f2 0%,#f2f2f2 10%,#3f9a3a 10%,#2f8a34 88%,#f2f2f2 88%);border:2px solid #d0d0d0"></div>

<h2 class="section-h why-head abs">Why Us?</h2>
<p class="why-lead abs">Aliquam molestie, mi et imperdiet euismod, dui purus auctor tellus, et interdum lacus lectus et ante.</p>

<div class="feature abs" style="left:90px">
  <div class="feature-icon">
    <svg width="50" height="50" viewBox="0 0 50 50"><circle cx="25" cy="25" r="20" fill="none" stroke="#333" stroke-width="5"/><circle cx="25" cy="25" r="8" fill="#333"/></svg>
  </div>
  <h3 class="feature-title">Nam fermentum</h3>
  <p class="copy">Sed accumsan sollicitudin sapien, sit amet adipiscing turpis gravida ac. In congue, neque ac lobortis volutpat..</p>
  <a class="feature-link" href="#">Read More</a>
</div>
<div class="feature abs" style="left:448px">
  <div class="feature-icon">
    <svg width="56" height="50" viewBox="0 0 56 50"><rect x="4" y="4" width="48" height="30" rx="3" fill="#333"/><path d="M16 4v30M28 4v30M40 4v30M4 19h48" stroke="#fff" stroke-width="2"/><path d="M28 34v10M16 46h24" stroke="#333" stroke-width="4"/></svg>
  </div>
  <h3 class="feature-title">Nam fermentum</h3>
  <p class="copy">Sed accumsan sollicitudin sapien, sit amet adipiscing turpis gravida ac. In congue, neque ac lobortis volutpat..</p>
  <a class="feature-link" href="#">Read More</a>
</div>
<div class="feature abs" style="left:808px">
  <div class="feature-icon">
    <svg width="52" height="50" viewBox="0 0 52 50"><path d="M6 14 Q22 2 38 10" fill="none" stroke="#333" stroke-width="5"/><path d="M22 8 L10 34" stroke="#333" stroke-width="5"/><path d="M20 46 L46 20 L46 46 Z" fill="#333"/></svg>
  </div>
  <h3 class="feature-title">Nam fermentum</h3>
  <p class="copy">Sed accumsan sollicitudin sapien, sit amet adipiscing turpis gravida ac. In congue, neque ac lobortis volutpat..</p>
  <a class="feature-link" href="#">Read More</a>
</div>

<section class="blog-band abs"></section>
<div class="blog-body abs">
  <h2 class="section-h">Blog Posts</h2>
  <p class="blog-kicker">Aliquam molestie mi et imperdiet euismod</p>
  <p class="copy">Dui purus auctor tellus, et interdum lacus lectus et ante. Sed accumsan sollicitudin sapien, sit amet adipiscing turpis gravida ac. In congue, neque ac lobortis volutpat, libero mauris varius mi, vitae suscipit ipsum ligula vitae risus.</p>
</div>
<a class="btn blog-btn abs" href="#">Read More</a>
<div class="blog-photo abs" role="img" aria-label="Gold crypto coins around a glowing green coin on a smartphone screen"></div>

<h2 class="section-h sub-head abs">Email Subscribe</h2>
<p class="sub-lead abs">Aliquam molestie, mi et imperdiet euismod, dui purus auctor tellus, et interdum lacus lectus et ante.</p>
<form class="sub-form abs"><span class="field">Enter Email Address</span><span class="btn">Sign Up</span></form>

<footer class="site-footer abs"></footer>
<div class="footer-mark abs">Brook Forge</div>
<nav class="footer-nav abs">
  <a href="#">Home</a><a href="#">About Us</a><a href="#">Services</a><a href="#">Why Us?</a><a href="#">Blog</a><a href="#">Contact Us</a>
</nav>
<p class="copyright abs">Copyright © 2018. Company Name All Right Reserved</p>
<div class="social abs"><span></span><span></span><span></span><span></span><span></span></div>

</body>
</html>
```